Business Card design for a company called Copper Vale HQ

I need a business card design for my oil fired boiler servicing company. I have a logo design already and Im just looking that incorporated into the business card design. card details; Copper Vale HQ
Oil Burner Servicing - Mid Ulster Area
Service Engineer - Dean Morrow
Mobile 07700900418
email - Copper.Vale.HQ@brandmail.test
www.coppervalehq.test
I carry out Servicing, Commissioning, Fault Finding, Warranty Validation
Target Market(s)
home owners with oil fired central heating
Industry/Entity Type
Business
Contact Information for Business Card
Copper Vale HQ
Tell. 07700900418
Web: www.coppervalehq.test
email Copper.Vale.HQ@Brandmail.Test
Servicing Fault Finding Commissioning Warranty Validation
Look and feel

```html
<!DOCTYPE html>
<html lang="en">
<head>
<meta charset="utf-8">
<title>Copper Vale HQ – Business Card</title>
<link rel="stylesheet" href="https://fonts.googleapis.com/css2?family=Arimo:wght@400;700&display=swap">
<style>
  :root {
    --green: #4cbf4f;
    --lime: #c6e04a;
    --white: #ffffff;
    --paper: #fdfdfd;
    --stage: #e9ece8;
    --ink-green: #4cbf4f;
  }
  * { margin: 0; padding: 0; box-sizing: border-box; }
  html, body {
    width: 1200px; height: 780px; overflow: hidden;
    background: var(--stage);
    font-family: "Arimo", Arial, sans-serif;
  }
  .card {
    position: absolute; left: 100px; top: 104px;
    width: 1000px; height: 572px;
    background: var(--paper);
    overflow: hidden;
    box-shadow: 0 6px 24px rgba(0,0,0,.12);
  }
  .card-art { position: absolute; inset: 0; }
  .brand {
    position: absolute; left: 56px; top: 140px;
    display: flex; align-items: center; gap: 16px;
  }
  .brand-dot {
    width: 62px; height: 62px; border-radius: 50%;
    background: var(--green);
  }
  .brand-name {
    font-size: 50px; font-weight: 700; color: var(--ink-green);
    letter-spacing: -1px; line-height: 1;
    white-space: nowrap;
  }
  .tagline {
    position: absolute; left: 136px; top: 212px;
    font-size: 13px; letter-spacing: 1.8px; color: var(--ink-green);
    text-transform: uppercase; white-space: nowrap;
  }
  .services {
    position: absolute; left: 66px; top: 312px;
    list-style: none;
  }
  .services li {
    display: flex; align-items: center; gap: 11px;
    font-size: 22px; color: var(--ink-green); line-height: 34px;
    white-space: nowrap;
  }
  .services li::before {
    content: ""; width: 11px; height: 11px; border-radius: 50%;
    background: var(--green);
  }
  .services li:nth-child(2) { padding-left: 20px; }
  .services li:nth-child(3) { padding-left: 40px; }
  .services li:nth-child(4) { padding-left: 60px; }
  .contact {
    position: absolute; right: 44px; top: 40px;
    text-align: right; color: var(--white);
  }
  .contact-name { font-size: 36px; font-weight: 700; line-height: 1.05; }
  .contact-role { font-size: 20px; margin-bottom: 24px; }
  .contact-line {
    display: flex; justify-content: flex-end; align-items: center; gap: 12px;
    font-size: 19px; line-height: 36px; white-space: nowrap;
  }
  .contact-line svg { width: 20px; height: 20px; flex: none; }
</style>
</head>
<body>
  <div class="card">
    <svg class="card-art" viewBox="0 0 1000 572" preserveAspectRatio="none" aria-hidden="true">
      <path d="M270 572 C360 530 430 460 462 360 C470 450 420 530 350 572 Z" fill="var(--lime)"/>
      <path d="M0 572 V556 C120 562 230 558 300 550 L320 572 Z" fill="var(--lime)"/>
      <path d="M720 0 H1000 V572 H340 C430 500 500 400 540 290 C580 180 620 60 720 0 Z" fill="var(--green)"/>
      <path d="M712 16 C628 66 588 186 552 296 C518 400 462 492 392 550" fill="none" stroke="var(--white)" stroke-width="6" stroke-linecap="round"/>
      <path d="M640 440 C720 478 790 502 880 512" fill="none" stroke="var(--white)" stroke-width="3" opacity=".5"/>
    </svg>

    <div class="brand">
      <span class="brand-dot"></span>
      <span class="brand-name">Copper Vale HQ</span>
    </div>
    <p class="tagline">Oil Burner Servicing - Mid Ulster Area</p>

    <ul class="services">
      <li>Servicing</li>
      <li>Commissioning</li>
      <li>Fault Finding</li>
      <li>Warranty Validation</li>
    </ul>

    <div class="contact">
      <p class="contact-name">Dean Morrow</p>
      <p class="contact-role">Service Engineer</p>
      <p class="contact-line">07700900418
        <svg viewBox="0 0 24 24" fill="var(--white)"><path d="M6.6 10.8a15 15 0 0 0 6.6 6.6l2.2-2.2c.3-.3.7-.4 1-.2 1.1.4 2.3.6 3.6.6.6 0 1 .4 1 1V20c0 .6-.4 1-1 1A17 17 0 0 1 3 4c0-.6.4-1 1-1h3.5c.6 0 1 .4 1 1 0 1.3.2 2.5.6 3.6.1.3 0 .7-.2 1z"/></svg>
      </p>
      <p class="contact-line">Copper.Vale.HQ@Brandmail.Test
        <svg viewBox="0 0 24 24" fill="none" stroke="var(--white)" stroke-width="2"><rect x="3" y="5" width="18" height="14" rx="1"/><path d="M3 6l9 7 9-7"/></svg>
      </p>
      <p class="contact-line">www.coppervalehq.test
        <svg viewBox="0 0 24 24" fill="none" stroke="var(--white)" stroke-width="2"><circle cx="12" cy="12" r="9"/><path d="M3 12h18M12 3c3 3 3 15 0 18M12 3c-3 3-3 15 0 18"/></svg>
      </p>
    </div>
  </div>
</body>
</html>
```